FREE BBQ for life if you win our business with your creative menu design

Looking for a 11x17 size menu. we are a full service BBQ restaurant. We have an upscale environment as well as up scale service. We offer 5 star dinning at a casual price. we are on route 66 and are proud of that. we offer the finest smoked meats. Specializing in smoked pork beef and bison. we have an old barn wood decor. we only use oak to smoke our meats. use a lot of tarnished metal as well as some string nail art. Looking for a menu that goes along our style. i have attached as many pictures as i could to give you a fill of how we do it out here.
PLEASE USE THE 11"X17" MENU TEMPLATE ATTACHED IN THE PROJECT BRIEF.
Target Market(s)
Cool people and there families.
Industry/Entity Type
Business
Requirements
Must have
- I have attached the Current menu we use. File pollards menu pub. Those are all the Items. There will be some changes as we but together the new menu. The prices are changing. but that should be an easy change as we go.
Nice to have
- We are getting away from the lunch dinner menu and going to an all day menu. so rather than coming with toast or bun we will now be asking as an option. I have attached a menu i tried to make as a sample of how we will be doing it. new menu single page and new menu single page flame. These are ideas i had but could not really make it work. so use them as an idea of what we are looking for but be creative.

```html
<!DOCTYPE html>
<html lang="en">
<head>
<meta charset="utf-8">
<title>Pollards BBQ – Fresh From the Grill Menu</title>
<link href="https://fonts.googleapis.com/css2?family=Bebas+Neue&family=Crimson+Text:wght@400;600;700&family=Rye&family=Oswald:wght@500;700&display=swap" rel="stylesheet">
<style>
:root{
  --wood-teal:#3b5a60;
  --wood-brown:#4e3d31;
  --wood-dark:#2a3236;
  --panel:rgba(16,20,24,.6);
  --orange:#e8782a;
  --white:#f3efe8;
  --flame:#f39a2c;
  --title-red:#5a140c;
  --blue-badge:#2a6fc0;
  --kids-blue:#3ea6d8;
  --kids-navy:#1f3e73;
}
*{margin:0;padding:0;box-sizing:border-box}
html,body{width:927px;height:1200px;overflow:hidden;background:var(--wood-dark)}
.menu{position:relative;width:927px;height:1200px;overflow:hidden;font-family:'Crimson Text',serif;color:var(--white)}
.wood{position:absolute;inset:0;background:linear-gradient(100deg,var(--wood-teal),var(--wood-brown) 45%,var(--wood-teal) 75%,#4a3a30)}
.deco{position:absolute}
.deco-star{left:-10px;top:-10px;width:320px;height:250px;border-radius:40%;background:radial-gradient(circle,rgba(140,136,128,.75),rgba(80,76,72,.2) 70%,transparent)}
.deco-plate-tr{left:800px;top:-40px;width:120px;height:90px;border-radius:50%;background:radial-gradient(rgba(138,106,74,.8),transparent 72%)}
.deco-metal-r{left:850px;top:60px;width:77px;height:130px;background:linear-gradient(rgba(154,150,142,.55),rgba(106,102,96,.3))}
.deco-string{left:730px;top:240px;width:197px;height:370px;background:linear-gradient(160deg,rgba(43,94,138,.55),rgba(196,98,30,.55) 55%,rgba(43,94,138,.45))}
.deco-sign-br{left:790px;top:650px;width:137px;height:470px;background:linear-gradient(180deg,rgba(106,74,42,.55),rgba(74,58,90,.55) 60%,rgba(122,74,44,.55))}
.deco-plate-l{left:0;top:290px;width:70px;height:350px;background:linear-gradient(90deg,rgba(122,90,122,.5),transparent)}
.deco-rust-l{left:0;top:700px;width:60px;height:170px;background:linear-gradient(90deg,rgba(122,80,48,.6),transparent)}
.deco-metal-bl{left:0;top:900px;width:70px;height:120px;background:linear-gradient(90deg,rgba(138,134,128,.5),transparent)}
.strip{position:absolute;left:0;right:0;top:1118px;height:50px;background:linear-gradient(#6a4a32,#4a3222)}
.tin{position:absolute;left:0;right:0;top:1168px;bottom:0;background:linear-gradient(#8e8e8e,#6e6e6e)}
.panel{position:absolute;left:56px;top:222px;width:808px;height:912px;background:var(--panel);border-radius:14px}

.title{position:absolute;left:328px;width:450px;top:38px;text-align:center}
.title-top{font-family:'Rye',serif;font-size:31px;line-height:1;color:var(--title-red);letter-spacing:1px}
.title-main{font-family:'Rye',serif;font-size:100px;line-height:1.1;letter-spacing:4px;color:var(--flame)}

.sec{position:absolute}
.sec h2{font-family:'Bebas Neue',sans-serif;font-weight:400;font-size:46px;line-height:1;color:var(--white);margin-bottom:10px}
.item{margin-bottom:9px;font-size:8.6px;line-height:1.45}
.item h3{font-weight:700;font-size:9.2px;color:var(--orange)}
.hl{color:var(--orange);font-weight:700;font-size:9.2px}
.lead{font-size:11px;line-height:1.45}
.lead strong{display:block;font-size:11.5px}
.list{font-size:8.8px;line-height:1.5}

.loyalty{position:absolute;left:76px;top:890px;width:220px;height:210px}
.loyalty-photo{position:absolute;left:36px;top:0;width:162px;height:162px;border-radius:50%;border:4px solid var(--white);background:radial-gradient(#6a3a22,#2a1810)}
.loyalty-name{position:absolute;left:36px;top:48px;width:162px;text-align:center;font-family:'Oswald',sans-serif;font-weight:700;font-size:48px;color:var(--kids-blue)}
.loyalty-bar{position:absolute;left:0;top:142px;width:216px;padding:6px 0;background:var(--blue-badge);transform:rotate(-2deg);text-align:center;font-family:'Bebas Neue',sans-serif;font-size:19px}
.loyalty-tag{position:absolute;left:40px;top:176px;width:148px;padding:4px 0;background:var(--orange);transform:rotate(-2deg);text-align:center;font-size:9.5px;line-height:1.1}

.kids{position:absolute;left:300px;top:956px;width:164px;height:150px}
.kids svg{position:absolute;inset:0}
.kids-line1{position:absolute;left:14px;top:8px;width:130px;text-align:center;font-family:'Bebas Neue',sans-serif;font-size:17px;background:var(--orange);transform:rotate(-4deg)}
.kids-line2{position:absolute;left:0;top:32px;width:164px;text-align:center;font-family:'Bebas Neue',sans-serif;font-size:26px;background:var(--kids-navy);transform:rotate(-3deg)}
.kids-line3{position:absolute;left:30px;top:76px;width:110px;text-align:center;font-family:'Bebas Neue',sans-serif;font-size:22px}

.brands{display:flex;align-items:center;gap:14px;margin:4px 0 8px}
.brand{display:flex;align-items:center;gap:5px;font-family:'Oswald',sans-serif;font-weight:500;font-size:17px}
.brand i{width:22px;height:22px;border-radius:50%;background:var(--white)}
</style>
</head>
<body>
<div class="menu">
  <div class="wood" role="img" aria-label="Weathered teal and brown barn wood planks"></div>
  <div class="deco deco-star" role="img" aria-label="Tarnished metal star decoration"></div>
  <div class="deco deco-plate-tr" role="img" aria-label="Rusty round metal plate"></div>
  <div class="deco deco-metal-r" role="img" aria-label="Tarnished metal plate"></div>
  <div class="deco deco-string" role="img" aria-label="BBQ string and nail art sign"></div>
  <div class="deco deco-sign-br" role="img" aria-label="Rustic painted wooden sign"></div>
  <div class="deco deco-plate-l" role="img" aria-label="Old painted metal sign"></div>
  <div class="deco deco-rust-l" role="img" aria-label="Rusty round metal disc"></div>
  <div class="deco deco-metal-bl" role="img" aria-label="Tarnished metal plate"></div>
  <div class="strip" role="img" aria-label="Wooden plank band"></div>
  <div class="tin" role="img" aria-label="Corrugated tin band"></div>

  <header class="title" role="img" aria-label="Fresh from the grill title in flames">
    <div class="title-top">FRESH FROM THE</div>
    <div class="title-main">GRILL</div>
  </header>

  <div class="panel"></div>

  <section class="sec" style="left:86px;top:256px;width:214px">
    <h2>APPETIZER</h2>
    <div class="item"><h3>King Rings</h3>Green Chili battered fried golden crispy 1" thick onion rings. 6.89</div>
    <div class="item"><h3>Deep Fried Pickles</h3>Crisp dill pickle chips battered and fried to a golden crispy brown 6.89</div>
    <div class="item"><h3>Fried Okra</h3>Okra is breaded then fried until golden. 6.89</div>
    <div class="item"><h3>Green Chili Waffle Fries</h3>Crispy waffle-cut Fries, topped with a savory blend of cheese, and New Mexico green chile. 7.49</div>
    <div class="item"><h3>KC Wild Wings</h3>Big, meaty pork wings, deep fried to a perfect golden brown, tossed in a hot and tangy Buffalo-style sauce, and served with spicy buttermilk ranch dressing on the side. 7.99</div>
    <div class="item"><h3>Sampler Platter</h3>Two KC Wild Wings, 6oz Fried Pickles, 3 King Rings. 7.99</div>
  </section>

  <section class="sec" style="left:86px;top:612px;width:244px">
    <h2>BISON</h2>
    <p class="lead" style="margin-bottom:12px"><strong>Heart Healthy</strong>Comes with 1 side dish and your choice of Texas toast, Kaiser bun, Whole wheat bread or Glutton Free bread</p>
    <div class="item"><h3>Bison Burger</h3>Smoked then grilled served with pepper jack cheese lettuce tomato pickle toped with spicy ranch. 12.59</div>
    <div class="item"><h3>Bison Brisket</h3>The belly of beast, smoked then sliced thin and grilled. Juicy and tender 18.65</div>
    <div class="item"><h3>Bison Steak</h3>12oz of lean healthy meat cooked to your desired temp. 34.56</div>
  </section>

  <section class="sec" style="left:356px;top:250px;width:430px">
    <h2 style="margin-bottom:6px">SMOKED</h2>
    <p class="lead" style="font-size:10.6px"><strong>Heart Healthy</strong>Comes with 1 side dish and your choice of Texas toast, Kaiser bun, Whole wheat bread or Glutton Free bread</p>
  </section>
  <section class="sec" style="left:356px;top:352px;width:210px">
    <div class="item"><h3>Baby Back Ribs</h3>Tender to the bone, finger licking good, never need a knife, best ribs you'll ever have.<br>Full Rack 19.96 Half Rack 10.49</div>
    <div class="item"><h3>St. Louis Ribs</h3>A nice big tender spare rib, slow smoked to tender that you can sink your teeth into.<br>16.45</div>
    <div class="item"><h3>Beef Brisket</h3>The most insane mouth watering smoky, moist, succulent piece of meat your mouth will ever have. 10.95</div>
    <div class="item"><h3>Pulled Pork</h3>Smoked for 18-20 hrs. then pulled and mixed with our signature base barbeque sauce.<br>9.59</div>
  </section>
  <section class="sec" style="left:612px;top:352px;width:205px">
    <div class="item"><h3>Sliced Pork</h3>Smoked juicy tenderloin sliced thin then grilled per order. 9.54</div>
    <div class="item"><h3>Smoked Turkey</h3>Breast meat smoked and sliced. Juicy and tender. 9.49</div>
    <div class="item"><h3>Smoked Chicken half</h3>Moist and juicy smoked Breast and thigh on the bone basted with our signature sauce on the grill. 13.59</div>
    <div class="item"><h3>Rib Eye</h3>12oz juicy steak grilled to your desired temp 21.95</div>
  </section>

  <section class="sec" style="left:354px;top:620px;width:220px">
    <h2>DESSERTS</h2>
    <div class="item"><h3>Peach Cobbler &amp; Ice Cream</h3>Served hot topped with ice cream 5.89</div>
    <div class="item"><h3>Cookies A-L-Mode</h3>2 hot gooey cookies topped with ice cream your choice chocolate chip or macadamia nut 5.89</div>
    <div class="item"><h3>Dessert of the week</h3>Ask your server for our special dessert of the week</div>
  </section>

  <section class="sec" style="left:354px;top:798px;width:200px">
    <h2>SIDE DISHES</h2>
    <div class="list">Green Chile Creamed Corn<br>Potato Salad<br>Baked Potato<br>Grilled Veggies<br>Baked Beans<br>Waffle Fries<br>Extra side 2.29</div>
  </section>

  <section class="sec" style="left:612px;top:548px;width:200px">
    <h2>PB CUSTOMS</h2>
    <div class="item"><h3>BBQ Tacos</h3>Three Tacos in blue and red shells with your choice of meat topped with shredded lettuce and Pico-D –BBQ and Spicy ranch.<br>(Excludes ribs and bison. ) 9.89</div>
    <div class="item"><span class="hl">Taco Tuesday</span> is a Must! 5.00 tacos all day</div>
    <div class="item"><h3>Rowdy Chicken Sandwich</h3>Skinless boneless chicken breasts breaded fried, topped with pepper jack cheese, lettuce, tomato onion and pickles. On a buttery grilled Texas toast.</div>
    <div class="item"><h3>Create Your Own Wrap</h3>Pick your own meat, cheese, the additionals and sauce.</div>
  </section>

  <section class="sec" style="left:610px;top:814px;width:200px">
    <h2>DRINKS</h2>
    <div class="item"><h3>Lemonade</h3>Regular, Strawberry, Watermelon Cherry, Peach 2.59</div>
    <div class="item" style="margin-bottom:0"><h3>Fountain</h3></div>
    <div class="brands">
      <span class="brand"><i></i>Fizzco</span>
      <span class="brand">Doc Pebble</span>
    </div>
    <div class="item">Fizzco, Doc Pebble, Root Beer, Alpine Fizz, Summit Splash, Diet Fizzco Diet Doc Pebble 1.89</div>
    <div class="item"><h3>Iced Teas</h3>Sweetened, Unsweetened 1.89</div>
  </section>

  <div class="loyalty">
    <div class="loyalty-photo" role="img" aria-label="Close-up photo of smoked barbecue meat"></div>
    <div class="loyalty-name">loopa</div>
    <div class="loyalty-bar">JOIN OUR CUSTOMER LOYALTY APP</div>
    <div class="loyalty-tag">Get FREE FOOD when you become a loyal customer.</div>
  </div>

  <div class="kids">
    <svg viewBox="0 0 164 150" aria-hidden="true"><polygon points="82,6 152,36 152,110 82,146 12,110 12,36" fill="#3ea6d8"/></svg>
    <div class="kids-line1">KIDS UNDER 4</div>
    <div class="kids-line2">EAT FREE !</div>
    <div class="kids-line3">SEE KIDS MENU</div>
  </div>
</div>
</body>
</html>
```